Birchlane Chiropractic Business Cards

Business cards with new logo design. Will upload copy of current card. We like the layout, but we need a new logo. Family, husband holding up baby toward sky, mom and other child standing next to him. We will probably want to include a catch phrase with logo. TBD

```html
<!DOCTYPE html>
<html lang="en">
<head>
<meta charset="utf-8">
<title>Birchlane Chiropractic – Business Cards</title>
<link href="https://fonts.googleapis.com/css2?family=Montserrat:wght@400;500;600&display=swap" rel="stylesheet">
<style>
  :root {
    --backdrop: #c4c4c4;
    --card-light: #dddcdd;
    --panel-light: #eeeced;
    --brand-red: #e63c24;
    --ink: #231f20;
    --white: #ffffff;
    --map-base: #f6f3ee;
    --map-road: #ebe5dc;
    --pin-blue: #2d86cc;
  }
  * { margin: 0; padding: 0; box-sizing: border-box; }
  html, body {
    width: 1200px; height: 1200px; overflow: hidden;
    background: var(--backdrop);
    font-family: "Montserrat", sans-serif;
  }
  .canvas { position: relative; width: 1200px; height: 1200px; }
  .card {
    position: absolute; top: 248px;
    width: 403px; height: 703px;
    border-radius: 28px;
    text-align: center;
  }
  .card--front { left: 128px; background: var(--card-light); color: var(--ink); }
  .card--back { left: 668px; background: var(--brand-red); color: var(--white); }

  .mark-panel {
    position: absolute; left: 48px; top: 30px;
    width: 308px; height: 308px;
    border-radius: 30px;
    background: var(--panel-light);
    display: flex; flex-direction: column; align-items: center; justify-content: center;
    gap: 22px;
  }
  .mark-panel__dot { width: 110px; height: 110px; border-radius: 50%; background: var(--brand-red); }
  .mark-panel__name { font-size: 34px; font-weight: 600; letter-spacing: 1px; color: var(--ink); }

  .wordmark {
    position: absolute; left: 0; width: 100%;
    font-weight: 600; line-height: 1;
  }
  .wordmark__name { display: block; font-size: 52px; letter-spacing: 1px; }
  .wordmark__trade { display: block; font-size: 38px; font-weight: 500; letter-spacing: 0.5px; margin-top: 22px; }
  .card--front .wordmark { top: 358px; color: var(--ink); }
  .card--back .wordmark { top: 551px; color: var(--white); }

  .person { position: absolute; left: 0; width: 100%; top: 510px; }
  .person__name { font-size: 27px; font-weight: 600; color: var(--brand-red); line-height: 34px; }
  .person__title { font-size: 19px; font-weight: 400; margin-top: 2px; }

  .contact { position: absolute; left: 0; width: 100%; top: 611px; font-size: 19px; line-height: 29px; }

  .map {
    position: absolute; left: 48px; top: 32px;
    width: 307px; height: 307px;
    border-radius: 30px;
    background: linear-gradient(160deg, var(--map-base), var(--map-road));
  }
  .map__pin { position: absolute; left: 141px; top: 104px; width: 32px; height: 48px; }

  .address { position: absolute; left: 0; width: 100%; top: 372px; font-size: 20px; line-height: 28px; }
</style>
</head>
<body>
<main class="canvas">
  <section class="card card--front" aria-label="Business card front">
    <div class="mark-panel">
      <span class="mark-panel__dot"></span>
      <span class="mark-panel__name">BIRCHLANE</span>
    </div>
    <h1 class="wordmark">
      <span class="wordmark__name">BIRCHLANE</span>
      <span class="wordmark__trade">CHIROPRACTIC</span>
    </h1>
    <div class="person">
      <p class="person__name">Dr. Daniel R. Whitcombe</p>
      <p class="person__title">Chiropractic Physician</p>
    </div>
    <div class="contact">
      <p>P : 503-555-0142</p>
      <p>w : www.whitcombechiropractic.com</p>
    </div>
  </section>

  <section class="card card--back" aria-label="Business card back">
    <div class="map" role="img" aria-label="Street map showing the clinic location">
      <svg class="map__pin" viewBox="0 0 32 48" aria-hidden="true">
        <path d="M16 0C7.2 0 0 7.2 0 16c0 11 16 32 16 32s16-21 16-32C32 7.2 24.8 0 16 0z" fill="var(--pin-blue)"/>
        <circle cx="16" cy="15" r="6" fill="var(--white)"/>
      </svg>
    </div>
    <div class="address">
      <p>2480 SE Maple Grove Town Center</p>
      <p>Dr. Millbrook, Oregon 97099</p>
      <p>P: 503-555-0142</p>
      <p>F: 503-555-0178</p>
    </div>
    <h2 class="wordmark">
      <span class="wordmark__name">BIRCHLANE</span>
      <span class="wordmark__trade">CHIROPRACTIC</span>
    </h2>
  </section>
</main>
</body>
</html>
```